"Beyond Marrow Cay" Fictional Book Cover

BEYOND MARROW CAY
By: Dale Pruitt

Here's the intro .

"It had been nearly forty years since Ted Larraby last went to the island from where he was raised. Three months earlier he never would have thought about ever coming back. But life is weird. Things happen quickly and plans change, especially when your very life is at stake. The reason he was going back wasn’t to see old friends...no, no, no. They’re all dead. Of all the kids he grew up with on the island who moved off, he’s the only one still alive. Why?"

Pretty much all just a Lumeno book, by the way.

Target Market(s)

fiction readers

Requirements
Must have
• Somewhat of a dark, mysterious cover is what I'd like to see. Use your imagination. I've never written a fiction book before so I'm very open to ideas

Needs to have my name, DALE PRUITT at the bottom. like my other books, all of which are non-fiction
Nice to have
• Mysterious is what I'm looking for. NOT A HORROR story though. More a guy who left the island years ago, but is being called back to escape the rat race of modern, consumerist culture.

Please remember this NEEDS to jump out as a thumbnail on Bookvale as people are browsing. Mainly the WORDS need to stick out. Lighter words on a say a blue background.

If you want to try to use the attached pic, or something like this, to reflect an island in the cover, that'd be good.

I've also uploaded a couple images I purchased from Pixelcrate, hopefully you can make something work with these.

```html
<!DOCTYPE html>
<html lang="en">
<head>
<meta charset="utf-8">
<title>Beyond Marrow Cay — Cover Wrap</title>
<link href="https://fonts.googleapis.com/css2?family=Fira+Sans:wght@400;500&family=Oswald:wght@700&display=swap" rel="stylesheet">
<style>
  :root {
    --night: #06081c;
    --title-red: #e8141b;
    --ink-white: #ffffff;
    --beam: #a9a9b0;
    --sky-top: #0b1a36;
    --sky-mid: #1f4a7a;
    --sky-low: #3a6d9c;
    --dusk: #c98a6c;
    --rock: #2c3d52;
    --steel-light: #f4f2ee;
    --steel-dark: #9a9ba0;
    --glow: #f3a040;
  }
  * { margin: 0; padding: 0; box-sizing: border-box; }
  html, body { width: 1200px; height: 858px; overflow: hidden; background: var(--night); }
  .cover-wrap {
    position: relative; width: 1200px; height: 858px;
    background: var(--night); overflow: hidden;
    font-family: "Fira Sans", sans-serif; color: var(--ink-white);
  }
  .front-art {
    position: absolute; left: 628px; top: 0; width: 572px; height: 858px;
    background:
      radial-gradient(ellipse 260px 180px at 60px 620px, rgba(201,138,108,.75), transparent 70%),
      linear-gradient(160deg, transparent 55%, var(--rock) 75%, #17202e 100%),
      linear-gradient(180deg, var(--sky-top) 0%, var(--sky-mid) 45%, var(--sky-low) 70%, #1a2433 100%);
  }
  .beam { position: absolute; left: 0; top: 0; }
  .back-title {
    position: absolute; left: 77px; top: 246px;
    font-family: "Fira Sans", sans-serif; font-weight: 500;
    font-size: 29px; letter-spacing: .5px; color: var(--title-red);
  }
  .blurb {
    position: absolute; left: 78px; top: 354px; width: 420px;
    font-size: 15.4px; line-height: 19.2px; font-weight: 500;
  }
  .blurb p + p { margin-top: 19.2px; }
  .isbn-box {
    position: absolute; left: 359px; top: 720px; width: 191px; height: 113px;
    background: var(--ink-white);
  }
  .spine-title, .spine-author {
    position: absolute; left: 596px; writing-mode: vertical-rl;
    font-family: "Fira Sans", sans-serif; font-weight: 500; white-space: nowrap;
    transform: translateX(-50%);
  }
  .spine-title { top: 30px; font-size: 28px; letter-spacing: 1px; color: var(--title-red); }
  .spine-author { top: 580px; font-size: 27px; color: var(--ink-white); }
  .front-author {
    position: absolute; left: 628px; width: 572px; top: 66px; text-align: center;
    font-weight: 500; font-size: 62px; color: var(--title-red); letter-spacing: .5px;
  }
  .front-title {
    position: absolute; left: 628px; width: 572px; top: 612px; text-align: center;
    font-family: "Oswald", sans-serif; font-weight: 700; text-transform: uppercase;
  }
  .front-title .line {
    display: block; font-size: 86px; line-height: 94px; letter-spacing: 1px;
    background: linear-gradient(180deg, var(--steel-light) 0%, var(--steel-dark) 55%, var(--steel-light) 100%);
    -webkit-background-clip: text; background-clip: text; color: transparent;
  }
  .front-title .glow {
    display: block; height: 2px; margin: 0 auto;
    background: linear-gradient(90deg, transparent, var(--glow), transparent);
  }
  .front-title .glow.first { width: 380px; margin-top: -6px; margin-bottom: 2px; }
  .front-title .glow.second { width: 460px; margin-top: -4px; }
</style>
</head>
<body>
<div class="cover-wrap">
  <div class="front-art" role="img" aria-label="Photograph of a white lighthouse on a rocky, pine-covered island cliff at dusk, with a bird in the blue sky"></div>

  <svg class="beam" width="1200" height="858" viewBox="0 0 1200 858" aria-hidden="true">
    <defs>
      <linearGradient id="beamFront" x1="0" x2="1" y1="0" y2="0">
        <stop offset="0" stop-color="#c8c8cf" stop-opacity=".75"/>
        <stop offset="1" stop-color="#e8e8ee" stop-opacity=".95"/>
      </linearGradient>
    </defs>
    <polygon points="0,206 628,236 628,282 0,332" fill="var(--beam)"/>
    <polygon points="628,236 968,252 968,264 628,282" fill="url(#beamFront)"/>
  </svg>

  <h2 class="back-title">BEYOND MARROW CAY</h2>
  <div class="blurb">
    <p>It had been nearly forty years since Ted Larraby<br>last went to the island from where he was raised.<br>Three months earlier he never would have thought<br>about ever coming back. But life is weird.<br>Things happen quickly and plans change, especially<br>when your very life is at stake.</p>
    <p>The reason he was going back wasn’t to see old<br>friends...no, no, no.<br>&nbsp;They’re all dead. Of all the kids he grew up with<br>on the island who moved off, he’s the only one<br>&nbsp;still alive. Why?</p>
  </div>
  <div class="isbn-box"></div>

  <div class="spine-title">BEYOND MARROW CAY</div>
  <div class="spine-author">Dale Pruitt</div>

  <div class="front-author">Dale Pruitt</div>
  <h1 class="front-title">
    <span class="line">Beyond</span>
    <span class="glow first"></span>
    <span class="line">Marrow Cay</span>
    <span class="glow second"></span>
  </h1>
</div>
</body>
</html>
```